Company Values Graphic

We are looking for a design of our company values that can be used in a variety of places including our website, mousepads, office posters, business cards, etc.

Notes:
- We'd rather have icons/art than photographs on the poster.... so more like an infographic
- The core value group headings are not required, but can be included if you think grouping the values works for your design
- We have a logo for our software product but that logo is not required
- We don't need/want clever images to accompany each value, but some images are fine
- BrightNest logo attached
- BrightNest colors are attached
- BrightNest logo is Nunito Sans ExtraBold 800
- BrightNest website uses Roboto

Our Values - Who we will work with (and who we will not)
The right set of values are essential to building and maintaining a culture that we all wake up eager to be a part of each day. They are foundational to all hiring and firing decisions. They attract the right people and repel the wrong ones.

BE HELPFUL
Make every person and place better because you are there.
Deliver wow with every interaction.

BE HUMBLE
Listen with every muscle.
Passionately help others first.
Seek first to understand.

BE HONEST
Earn trust every day.
Be open and direct.
Treat everyone with fairness and respect.

BE HUMAN
Celebrate passion and action.
Create an environment where people are authentic.
Hire great people and expect a lot from them

BE COURAGEOUS
Dare mighty things.
Make and honor commitments.
All great things start with a small act of courage applied at the right moment.

```html
<!DOCTYPE html>
<html lang="en">
<head>
<meta charset="utf-8">
<title>BrightNest – Our Values</title>
<link href="https://fonts.googleapis.com/css2?family=Nunito+Sans:wght@800&family=Roboto:wght@400;700;900&display=swap" rel="stylesheet">
<style>
  :root {
    --stage: #d0d0d0;
    --paper: #ffffff;
    --header: #ff9a00;
    --ink: #111111;
    --helpful: #4b9cf5;
    --humble: #ff5a00;
    --honest: #ff9a00;
    --human: #8a00ff;
    --courageous: #0a7d1a;
  }
  * { box-sizing: border-box; margin: 0; padding: 0; }
  html, body { width: 888px; height: 1200px; overflow: hidden; }
  body { background: var(--stage); font-family: "Roboto", sans-serif; position: relative; }

  .poster {
    position: absolute; left: 46px; top: 79px; width: 797px; height: 1031px;
    background: var(--paper); overflow: hidden;
  }
  .header-band {
    position: absolute; left: 0; top: 0; width: 100%; height: 396px; background: var(--header);
  }
  .header-notch { position: absolute; left: 377px; top: 363px; }
  .brand-box {
    position: absolute; left: 172px; top: 0; width: 457px; height: 150px;
    background: var(--paper); border-radius: 0 0 24px 24px;
    display: flex; align-items: center; justify-content: center; gap: 18px;
  }
  .brand-dot { width: 58px; height: 58px; border-radius: 50%; background: var(--humble); }
  .brand-name {
    font-family: "Nunito Sans", sans-serif; font-weight: 800; font-size: 50px;
    color: var(--ink); letter-spacing: -0.5px;
  }
  .title {
    position: absolute; left: 0; top: 186px; width: 100%; text-align: center;
    font-weight: 900; font-size: 66px; line-height: 1; color: var(--paper);
  }
  .intro {
    position: absolute; left: 34px; top: 256px; width: 729px; text-align: center;
    font-weight: 700; font-size: 16.4px; line-height: 22px; color: var(--paper);
  }
  .orbit { position: absolute; left: 0; top: 0; }

  .value {
    position: absolute; height: 94px; border: 1.5px solid; border-radius: 47px;
    display: flex; flex-direction: column; justify-content: center;
    background: var(--paper);
  }
  .value-icon {
    position: absolute; width: 80px; height: 80px; border-radius: 50%;
    box-shadow: 0 2px 6px rgba(0,0,0,.25);
  }
  .value h2 { font-weight: 900; font-size: 26px; line-height: 1; margin-bottom: 5px; }
  .value p { font-size: 13px; line-height: 15.5px; color: var(--ink); }

  .helpful { left: 288px; top: 431px; width: 353px; padding-left: 39px; padding-right: 20px; border-color: var(--helpful); }
  .helpful h2, .helpful-icon { color: var(--helpful); }
  .helpful-icon { left: 222px; top: 442px; background: var(--helpful); }

  .humble { left: 422px; top: 544px; width: 349px; padding-left: 63px; padding-right: 20px; border-color: var(--humble); }
  .humble h2 { color: var(--humble); }
  .humble-icon { left: 360px; top: 556px; background: var(--humble); }

  .honest { left: 434px; top: 658px; width: 338px; padding-left: 51px; padding-right: 30px; border-color: var(--honest); }
  .honest h2 { color: var(--honest); }
  .honest-icon { left: 388px; top: 664px; background: var(--honest); }

  .human { left: 422px; top: 772px; width: 351px; padding-left: 65px; padding-right: 14px; border-color: var(--human); }
  .human h2 { color: var(--human); }
  .human-icon { left: 357px; top: 777px; background: var(--human); }

  .courageous { left: 286px; top: 885px; width: 354px; padding-left: 40px; padding-right: 14px; border-color: var(--courageous); }
  .courageous h2 { color: var(--courageous); }
  .courageous-icon { left: 219px; top: 887px; background: var(--courageous); }
</style>
</head>
<body>
<main class="poster">
  <div class="header-band"></div>
  <svg class="header-notch" width="50" height="34" viewBox="0 0 50 34"><polygon points="0,34 25,0 50,34" fill="#ffffff"/></svg>

  <div class="brand-box">
    <span class="brand-dot"></span>
    <span class="brand-name">BrightNest</span>
  </div>

  <h1 class="title">OUR VALUES</h1>
  <p class="intro">Who we will work with (and who we will not) The right set of values are essential to building and maintaining a culture that we all wake up eager to be a part of each day. They are foundational to all hiring and firing decisions. They attract the right people and repel the wrong ones.</p>

  <svg class="orbit" width="797" height="1031" viewBox="0 0 797 1031">
    <defs>
      <filter id="soft" x="-20%" y="-20%" width="140%" height="140%">
        <feDropShadow dx="0" dy="2" stdDeviation="3" flood-color="#000" flood-opacity="0.18"/>
      </filter>
      <radialGradient id="warm" cx="50%" cy="55%" r="60%">
        <stop offset="0%" stop-color="#ff9a00"/>
        <stop offset="60%" stop-color="#ff5a00"/>
        <stop offset="100%" stop-color="#ff1a00"/>
      </radialGradient>
    </defs>
    <circle cx="182" cy="708" r="210" fill="#ffffff" filter="url(#soft)"/>
    <circle cx="182" cy="708" r="175" fill="none" stroke="#333" stroke-width="0.8" stroke-dasharray="3 2"/>
    <circle cx="182" cy="708" r="144" fill="#ffffff" filter="url(#soft)"/>
    <circle cx="182" cy="708" r="104" fill="url(#warm)" role="img" aria-label="Warm brand colour accent"/>
    <circle cx="201" cy="531" r="13" fill="var(--helpful)"/>
    <circle cx="331" cy="609" r="13" fill="var(--humble)"/>
    <circle cx="357" cy="706" r="13" fill="var(--honest)"/>
    <circle cx="323" cy="805" r="13" fill="var(--human)"/>
    <circle cx="201" cy="883" r="13" fill="var(--courageous)"/>
  </svg>

  <section class="value helpful">
    <h2>BE HELPFUL</h2>
    <p>Make every person and place better because you are there.Deliver wow with every interaction.</p>
  </section>
  <div class="value-icon helpful-icon" role="img" aria-label="Icon of a person helping another with a speech bubble"></div>

  <section class="value humble">
    <h2>BE HUMBLE</h2>
    <p>Listen with every muscle.Passionately help others first.Seek first to understand.</p>
  </section>
  <div class="value-icon humble-icon" role="img" aria-label="Icon of a humble person"></div>

  <section class="value honest">
    <h2>BE HONEST</h2>
    <p>Earn trust every day.Be open and direct.Treat everyone with fairness and respect.</p>
  </section>
  <div class="value-icon honest-icon" role="img" aria-label="Icon of a person with hand on heart"></div>

  <section class="value human">
    <h2>BE HUMAN</h2>
    <p>Celebrate passion and action.Create an environment where people are authentic.Hire great people and expect a lot from them.</p>
  </section>
  <div class="value-icon human-icon" role="img" aria-label="Icon of a group of people"></div>

  <section class="value courageous">
    <h2>BE COURAGEOUS</h2>
    <p>Dare mighty things.Make and honor commitments. All great things start with a small act of courage applied at the right moment.</p>
  </section>
  <div class="value-icon courageous-icon" role="img" aria-label="Icon of a person planting a flag on a summit"></div>
</main>
</body>
</html>
```